Company Profile
Corvane Logistics Sdn Bhd is a well established and experienced freight forwarder in Kuala Lumpur, Malaysia. We specialize in air and sea forwarding, Custom Brokerage and regulatory compliance services, inland transportation,
overseas freighting and warehousing and distribution management. With our dedicated qualified and experienced professionals, we are fully committed to serving our clients.

Our Mission
Based on the motto “Quick, Reliable and Polite”, Corvane Logistics is dedicated to upholding the following three points corporate philosophy:
1. Adhering to the principle that “the customer always comes first”.
2. Contributing to the development of the local community.
3. Making it our duty to be responsible and sincere.

Our Edge
• One-Stop Logistics Solutions
• Extensive Network Throughout Malaysia
• Highly Qualified and Experienced Pool of Professionals
• Comprehensive IT Solutions
• Innovative and Customer-focused Solutions
• Flexible and Consistent in Managing Exceptions
• Total Supply Chain Visibility

Target Market(s)

We sell the logistics services to all the industry in Malaysia. (ONE Stop Logistics Solutions)

Industry/Entity Type

Logistic

Contact Information for Business Card

I want the back of the card to be white with the logo and slogan. i would like to see the logo on the front with the general info.

Requirements
Must have
• Name, Title, Office, Cell, Fax, Email, Address, Website
Nice to have
• Modern Design Business Card

```html
<!DOCTYPE html>
<html lang="en">
<head>
<meta charset="utf-8">
<title>Corvane Logistics – Business Card</title>
<link rel="stylesheet" href="https://fonts.googleapis.com/css2?family=Questrial&display=swap">
<style>
  :root {
    --bg: #ececec;
    --card-front: #eef0f2;
    --card-back: #ffffff;
    --blue: #2f86cc;
    --blue-dark: #2467b0;
    --grey-band: #a9abae;
    --ink: #555a60;
    --ink-dark: #3b3f44;
    --white: #ffffff;
  }
  * { margin: 0; padding: 0; box-sizing: border-box; }
  html, body {
    width: 1200px; height: 797px; overflow: hidden;
    background: var(--bg);
    font-family: "Questrial", "Century Gothic", sans-serif;
  }
  .stage { position: relative; width: 1200px; height: 797px; }
  .card {
    position: absolute; top: 250px;
    width: 520px; height: 297px;
    border-radius: 3px;
    box-shadow: 0 6px 16px rgba(0,0,0,0.12);
    overflow: hidden;
  }
  .card--front { left: 50px; background: var(--card-front); }
  .card--back { left: 630px; background: var(--card-back); }

  .brand {
    display: flex; align-items: center; gap: 10px;
    font-size: 24px; letter-spacing: 0.5px; white-space: nowrap;
    color: var(--ink-dark);
  }
  .brand__dot { width: 14px; height: 14px; border-radius: 50%; background: var(--blue); flex: none; }
  .card--front .brand { position: absolute; top: 52px; right: 34px; }

  .back-lockup {
    position: absolute; top: 50%; left: 50%; transform: translate(-50%, -50%);
    display: flex; flex-direction: column; align-items: center; gap: 10px;
  }
  .back-lockup .brand { font-size: 28px; }
  .slogan {
    color: var(--blue); font-size: 13px; letter-spacing: 2px; text-transform: uppercase;
    white-space: nowrap;
  }

  .person { position: absolute; left: 40px; top: 112px; }
  .person__name {
    color: var(--blue-dark); font-size: 17px; font-weight: 700;
    letter-spacing: 0.6px; text-transform: uppercase;
  }
  .person__title { color: var(--ink); font-size: 13px; margin-top: 2px; }

  .address {
    position: absolute; right: 34px; top: 112px;
    text-align: right; color: var(--ink-dark); font-size: 12.5px; line-height: 1.35;
  }

  .contacts {
    position: absolute; left: 40px; top: 166px;
    list-style: none; color: var(--ink-dark); font-size: 12.5px; line-height: 1;
  }
  .contacts li { display: flex; align-items: center; gap: 9px; margin-bottom: 4px; }
  .contacts__label { color: var(--blue-dark); width: 36px; }
  .contacts svg { width: 13px; height: 13px; flex: none; }

  .band { position: absolute; left: 0; bottom: 0; width: 520px; height: 46px; }
</style>
</head>
<body>
<main class="stage">

  <section class="card card--front" aria-label="Business card front">
    <div class="brand"><span class="brand__dot"></span><span>Corvane Logistics</span></div>

    <div class="person">
      <p class="person__name">Mira Halvorsen</p>
      <p class="person__title">General Manager</p>
    </div>

    <p class="address">48 Jalan Tasek Perdana<br>Kuala Lumpur, 50480</p>

    <ul class="contacts">
      <li>
        <svg viewBox="0 0 13 13"><rect width="13" height="13" rx="2" fill="#2f86cc"/><path d="M4 3 L5.5 3 L6 5 L5 5.8 Q6 7.8 7.2 8 L8 7 L10 7.5 L10 9 Q6 10 3.5 4.5 Z" fill="#fff"/></svg>
        <span class="contacts__label">Office</span><span>03 8841 2760</span>
      </li>
      <li>
        <svg viewBox="0 0 13 13"><rect width="13" height="13" rx="2" fill="#2f86cc"/><rect x="4.5" y="2.5" width="4" height="8" rx="0.8" fill="none" stroke="#fff" stroke-width="1"/><circle cx="6.5" cy="9" r="0.5" fill="#fff"/></svg>
        <span class="contacts__label">Cell</span><span>012 674 3195</span>
      </li>
      <li>
        <svg viewBox="0 0 13 13"><rect width="13" height="13" rx="2" fill="#2f86cc"/><rect x="3" y="5.5" width="7" height="4" fill="none" stroke="#fff" stroke-width="1"/><rect x="4.5" y="3" width="4" height="2.5" fill="none" stroke="#fff" stroke-width="0.9"/></svg>
        <span class="contacts__label">Fax</span><span>03 8841 2761</span>
      </li>
      <li>
        <svg viewBox="0 0 13 13"><rect width="13" height="13" rx="2" fill="#2f86cc"/><rect x="3" y="4" width="7" height="5" fill="none" stroke="#fff" stroke-width="1"/><path d="M3 4 L6.5 7 L10 4" fill="none" stroke="#fff" stroke-width="1"/></svg>
        <span class="contacts__label">Email</span><span>info@corvane.com</span>
      </li>
      <li>
        <svg viewBox="0 0 13 13"><rect width="13" height="13" rx="2" fill="#2f86cc"/><circle cx="6.5" cy="6.5" r="3.5" fill="none" stroke="#fff" stroke-width="0.9"/><ellipse cx="6.5" cy="6.5" rx="1.5" ry="3.5" fill="none" stroke="#fff" stroke-width="0.8"/><path d="M3 6.5 H10" stroke="#fff" stroke-width="0.8"/></svg>
        <span class="contacts__label">Web</span><span>www.corvane.com</span>
      </li>
    </ul>

    <svg class="band" viewBox="0 0 520 46" preserveAspectRatio="none" aria-hidden="true">
      <polygon points="0,26 262,26 274,16 520,16 520,46 0,46" fill="#2f86cc"/>
      <polygon points="0,24 260,24 272,14 520,14 520,17 274,17 262,27 0,27" fill="#eef0f2"/>
      <polygon points="0,30 262,30 262,40 0,40" fill="#a9abae"/>
      <rect x="0" y="40" width="520" height="6" fill="#2f86cc"/>
    </svg>
  </section>

  <section class="card card--back" aria-label="Business card back">
    <div class="back-lockup">
      <div class="brand"><span class="brand__dot"></span><span>Corvane Logistics</span></div>
      <p class="slogan">Quick, Reliable and Polite</p>
    </div>
  </section>

</main>
</body>
</html>
```